Q-Forma Stationary Package
Nimble Forma
Q-Forma Stationary Package - Internet Services
Creative Brief
Professional
Tom Gaskin
President and CEO
P.O. Box 4352 Burlington, NJ 08016
Tom.Gaskin@Q-FormaLLC.example
www.Q-FormaLLC.example
I am interested in seeing business card designs in both horizontal and vertical styles. My company provided technical consulting for the PGB Veterans, KRTU, KRTU Sergeants, KRTU Lieutenants and Halvern PD Senior Officers’ Association. I would like their logos on my card either on the front or the back listed under the words "Technical Consulting." You can find their logos located at https://www.filevault.example/s/83k2m1q7zpwe4tx/consulting.zip?dl=0. Unfortunately, some of these logos are only available from me in low-resolution.

```html
<!DOCTYPE html>
<html lang="en">
<head>
<meta charset="utf-8">
<title>Q-Forma Business Card</title>
<link href="https://fonts.googleapis.com/css2?family=Roboto+Condensed:wght@400;700&family=Roboto:wght@400;700&display=swap" rel="stylesheet">
<style>
  :root {
    --bg: #e6e8eb;
    --card-white: #f7f8f9;
    --card-black: #0d0e10;
    --brand-blue: #1e9ad6;
    --brand-blue-light: #4fc0ec;
    --brand-navy: #1b3f73;
    --swoosh-grey: #b9bec4;
    --badge-grey: #2c3036;
    --text-dark: #1f2a3a;
    --text-muted: #9aa3ad;
    --text-white: #ffffff;
  }
  * { margin: 0; padding: 0; box-sizing: border-box; }
  html, body { width: 1200px; height: 901px; overflow: hidden; }
  body {
    background: var(--bg);
    font-family: "Roboto", Arial, sans-serif;
    display: flex;
    align-items: center;
    justify-content: center;
    gap: 60px;
  }
  .card {
    position: relative;
    width: 520px;
    height: 310px;
    border-radius: 30px;
    overflow: hidden;
    box-shadow: 0 10px 30px rgba(0,0,0,0.18);
  }
  .card-front { background: var(--card-white); }
  .card-back {
    background: var(--card-black);
    display: flex;
    flex-direction: column;
    align-items: center;
    justify-content: center;
    gap: 26px;
  }
  .wave { position: absolute; inset: 0; width: 100%; height: 100%; }
  .brand {
    position: absolute;
    left: 36px;
    top: 46px;
    display: flex;
    align-items: center;
    gap: 10px;
  }
  .brand-dot {
    width: 16px; height: 16px;
    border-radius: 50%;
    background: var(--brand-blue);
  }
  .brand-name {
    font-family: "Roboto Condensed", Arial, sans-serif;
    font-weight: 700;
    font-size: 40px;
    color: var(--brand-navy);
    letter-spacing: 0.5px;
  }
  .person {
    position: absolute;
    left: 292px;
    top: 58px;
  }
  .person-name {
    font-family: "Roboto Condensed", Arial, sans-serif;
    font-weight: 400;
    font-size: 22px;
    color: var(--text-dark);
    text-transform: uppercase;
    letter-spacing: 0.5px;
  }
  .person-title {
    font-size: 12px;
    color: var(--brand-blue);
    margin-top: 3px;
  }
  .contacts {
    position: absolute;
    right: 34px;
    top: 188px;
    list-style: none;
    text-align: right;
    color: var(--text-white);
    font-size: 11px;
    line-height: 21px;
  }
  .contacts li { display: flex; align-items: center; justify-content: flex-end; gap: 8px; }
  .contacts svg { width: 10px; height: 10px; fill: var(--text-white); flex: none; }
  .contacts .no-icon { padding-right: 18px; }
  .back-brand {
    display: flex;
    align-items: center;
    gap: 12px;
  }
  .back-brand .brand-name { color: var(--brand-blue-light); font-size: 52px; }
  .back-brand .brand-dot { width: 20px; height: 20px; background: var(--brand-blue-light); }
  .consulting { text-align: center; }
  .consulting-title {
    font-family: "Roboto Condensed", Arial, sans-serif;
    font-size: 12px;
    color: var(--text-muted);
    text-transform: uppercase;
    letter-spacing: 2px;
    margin-bottom: 12px;
  }
  .partner-badges {
    list-style: none;
    display: flex;
    gap: 14px;
    justify-content: center;
  }
  .partner-badge {
    width: 36px; height: 36px;
    border-radius: 50%;
    background: var(--badge-grey);
  }
</style>
</head>
<body>
  <section class="card card-front">
    <svg class="wave" viewBox="0 0 520 310" preserveAspectRatio="none" aria-hidden="true">
      <path d="M0 150 C120 120 220 190 330 150 C410 122 470 110 520 118 L520 310 L0 310 Z" fill="var(--swoosh-grey)"/>
      <path d="M0 165 C120 135 220 205 330 165 C410 137 470 125 520 133 L520 310 L0 310 Z" fill="var(--brand-blue)"/>
      <path d="M0 240 C150 200 300 300 520 230 L520 310 L0 310 Z" fill="var(--brand-blue-light)" opacity="0.35"/>
    </svg>
    <div class="brand">
      <span class="brand-dot"></span>
      <span class="brand-name">Q-Forma</span>
    </div>
    <div class="person">
      <h1 class="person-name">Tom Gaskin</h1>
      <p class="person-title">President and CEO</p>
    </div>
    <ul class="contacts">
      <li>P.O. Box 4352
        <svg viewBox="0 0 10 10"><path d="M5 0a3.5 3.5 0 0 0-3.5 3.5C1.5 6 5 10 5 10s3.5-4 3.5-6.5A3.5 3.5 0 0 0 5 0zm0 5a1.5 1.5 0 1 1 0-3 1.5 1.5 0 0 1 0 3z"/></svg></li>
      <li class="no-icon">Burlington, NJ 08016</li>
      <li>Tom.Gaskin@Q-FormaLLC.example
        <svg viewBox="0 0 10 10"><path d="M0 2h10v6H0z"/></svg></li>
      <li>www.Q-FormaLLC.example
        <svg viewBox="0 0 10 10"><circle cx="5" cy="5" r="5"/></svg></li>
    </ul>
  </section>

  <section class="card card-back">
    <div class="back-brand">
      <span class="brand-dot"></span>
      <span class="brand-name">Q-Forma</span>
    </div>
    <div class="consulting">
      <p class="consulting-title">Technical Consulting</p>
      <ul class="partner-badges">
        <li class="partner-badge" role="img" aria-label="PGB Veterans badge"></li>
        <li class="partner-badge" role="img" aria-label="KRTU badge"></li>
        <li class="partner-badge" role="img" aria-label="KRTU Sergeants badge"></li>
        <li class="partner-badge" role="img" aria-label="KRTU Lieutenants badge"></li>
        <li class="partner-badge" role="img" aria-label="Halvern PD Senior Officers’ Association badge"></li>
      </ul>
    </div>
  </section>
</body>
</html>
```